Business Card Design Project

A dual branded business card.

We have 2 business's: keyLeap and keyLeap360º. keyLeap is an online education marketplace that helps students fid great courses and classes (from learn to surf, to vocational training courses).

keyLeap360º is an agency that helps primarily vocational course providers with their online marketing and student enrolments.

Target Market(s)

Manager and Marketing Manager / CEOs of VEPI, University, Vocational Course Providers (RTOs)

Industry/Entity Type

Education

Requirements
Must have
• Brett Holloway
CEO

7-19 Ferris Lane, Torquay Vic 3228
Phone: 1300 584 916
Mobile: 0417 298 605
Email: brett@keyleap.com.au

Both Logos
Nice to have
• I nice way to combine the 2 brands which act as related but separate business's.

Essentially keyLeap is a marketplace which enable schools to get more student leads through the keyLeap.com.au platform.

keyLeap360º is an agency where we deliver online marketing services including: Google / Facebook PPC, SEO, Retargeting, Website Development and design, Student Enrolment Intelligence, and more... Essentially and online agency specifically servicing the education sector.

keyLeap
Australia's Education Marketplace with over 2,500 Teachers and Schools Australia wide (subject to change)

keyLeap360º
Digital Marketing Education (subject to change)

Should not have
• Not cluttered, not cheap looking, needs to have digital agency quality...

```html
<!DOCTYPE html>
<html lang="en">
<head>
<meta charset="utf-8">
<title>keyLeap / keyLeap360º business cards</title>
<link rel="stylesheet" href="https://fonts.googleapis.com/css2?family=Open+Sans:wght@400;700;800&display=swap">
<style>
  :root {
    --bg: #ececec;
    --card: #ffffff;
    --band-light: #3d9ad6;
    --band-dark: #1f6aa8;
    --accent-green: #7cc142;
    --brand-blue: #1a63a0;
    --text: #333333;
    --rule: #9a9a9a;
  }
  * { margin: 0; padding: 0; box-sizing: border-box; }
  html, body { width: 1200px; height: 402px; overflow: hidden; background: var(--bg); }
  body { font-family: "Open Sans", Arial, sans-serif; color: var(--text); }
  .stage { position: relative; width: 1200px; height: 402px; }

  .card {
    position: absolute; top: 57px; width: 519px; height: 292px;
    background: var(--card); border-radius: 22px; overflow: hidden;
    box-shadow: 0 3px 10px rgba(0,0,0,.18);
  }
  .card--market { left: 57px; }
  .card--agency { left: 622px; }

  .card__band { position: absolute; top: 0; bottom: 0; width: 54px; }
  .card__stripe { position: absolute; top: 0; bottom: 0; width: 3px; background: var(--accent-green); }
  .card--market .card__band { left: 0; background: linear-gradient(90deg, var(--band-light), var(--band-dark)); }
  .card--market .card__stripe { left: 56px; }
  .card--agency .card__band { right: 0; background: linear-gradient(90deg, var(--band-dark), var(--band-light)); }
  .card--agency .card__stripe { right: 57px; }

  .card__content { position: absolute; top: 0; bottom: 0; }
  .card--market .card__content { left: 95px; }
  .card--agency .card__content { left: 33px; }

  .brand-name {
    position: absolute; white-space: nowrap; font-weight: 800;
    color: var(--brand-blue); letter-spacing: -1px; line-height: 1;
  }
  .card--market .brand-name { top: 34px; left: 6px; font-size: 72px; }
  .card--agency .brand-name { top: 48px; left: 0; font-size: 54px; }

  .holder { position: absolute; top: 166px; left: 0; font-size: 15.5px; white-space: nowrap; }
  .holder__name { font-weight: 700; color: var(--brand-blue); }
  .holder__role { color: var(--brand-blue); }

  .contacts { position: absolute; top: 218px; left: 0; list-style: none; font-size: 14px; line-height: 19.5px; }
  .contacts li { display: flex; align-items: center; gap: 6px; white-space: nowrap; }
  .contacts svg { width: 12px; height: 12px; fill: var(--accent-green); flex: none; }

  .divider { position: absolute; top: 232px; left: 185px; width: 1px; height: 48px; background: var(--rule); }
  .address { position: absolute; top: 238px; left: 208px; font-size: 14px; line-height: 19.5px; white-space: nowrap; }
</style>
</head>
<body>
<div class="stage">

  <section class="card card--market">
    <div class="card__band"></div>
    <div class="card__stripe"></div>
    <div class="card__content">
      <div class="brand-name">keyLeap</div>
      <p class="holder"><span class="holder__name">Brett Holloway,</span> <span class="holder__role">CEO</span></p>
      <ul class="contacts">
        <li><svg viewBox="0 0 12 12"><path d="M3 1l2 2.5-1.2 1.3c.6 1.3 1.6 2.3 2.9 2.9L8 6.5 10.5 8.5 9.6 10.4C5.5 10.4 1.6 6.5 1.6 2.4z"/></svg>1300 584 916</li>
        <li><svg viewBox="0 0 12 12"><path d="M3.5 0.5h5a1 1 0 0 1 1 1v9a1 1 0 0 1-1 1h-5a1 1 0 0 1-1-1v-9a1 1 0 0 1 1-1zM4 2v6.5h4V2zM6 9.3a.7.7 0 1 0 0 1.4.7.7 0 0 0 0-1.4z"/></svg>0417 298 605</li>
        <li><svg viewBox="0 0 12 12"><path d="M1 4.5L6 1.5l5 3V10.5H1zM2 5l4 2.6L10 5 6 2.7z"/></svg>brett@keyleap.com.au</li>
      </ul>
      <div class="divider"></div>
      <p class="address">7-19 Ferris Lane<br>Kelvale Vic 3241</p>
    </div>
  </section>

  <section class="card card--agency">
    <div class="card__band"></div>
    <div class="card__stripe"></div>
    <div class="card__content">
      <div class="brand-name">keyLeap360º</div>
      <p class="holder"><span class="holder__name">Brett Holloway,</span> <span class="holder__role">CEO</span></p>
      <ul class="contacts">
        <li><svg viewBox="0 0 12 12"><path d="M3 1l2 2.5-1.2 1.3c.6 1.3 1.6 2.3 2.9 2.9L8 6.5 10.5 8.5 9.6 10.4C5.5 10.4 1.6 6.5 1.6 2.4z"/></svg>1300 584 916</li>
        <li><svg viewBox="0 0 12 12"><path d="M3.5 0.5h5a1 1 0 0 1 1 1v9a1 1 0 0 1-1 1h-5a1 1 0 0 1-1-1v-9a1 1 0 0 1 1-1zM4 2v6.5h4V2zM6 9.3a.7.7 0 1 0 0 1.4.7.7 0 0 0 0-1.4z"/></svg>0417 298 605</li>
        <li><svg viewBox="0 0 12 12"><path d="M1 4.5L6 1.5l5 3V10.5H1zM2 5l4 2.6L10 5 6 2.7z"/></svg>brett@keyleap.com.au</li>
      </ul>
      <div class="divider"></div>
      <p class="address">7-19 Ferris Lane<br>Kelvale Vic 3241</p>
    </div>
  </section>

</div>
</body>
</html>
```